Life Coaching and Career Coaching company needs new website with bold, modern, videos

We need a whole new website that is heavy on video. We are a small company who sells personal wellbeing services like career coaching, life coaching, and group coaching programs. The programs all help people design a better life.
FULL BRIEF ATTACHED and STYLE GUIDE
Also, look at https://www.pinevaultery.com/coaching and corvanly.com and https://www.tarnwick.life/ for a small amount of inspiration.

Industry/Entity Type

personal well-being/life coaching/career coaching

Number of Pages Required

3 page

Other font styles liked:
• fonts are in the brief

Requirements
Must have
• read the brief please - it's all in there. (things like the look, feel, how it will have lots of video, etc,)
Nice to have
• something really different looking and breakthrough. visually stunning. very trustworthy. Please read the brief, its all in there.
Should not have
• should not look like other life coaching websites. must have video!

```html
<!DOCTYPE html>
<html lang="en">
<head>
<meta charset="utf-8">
<title>Wayform Project – Life Coaching and Career Coaching</title>
<link href="https://fonts.googleapis.com/css2?family=Syncopate:wght@400;700&family=Montserrat:wght@400;500;600;700&display=swap" rel="stylesheet">
<style>
:root{
  --plum:#4a1450;
  --plum-deep:#2e0c35;
  --coral:#f2675f;
  --teal:#0c504d;
  --teal-dark:#0a3f3d;
  --blush:#f9e5df;
  --ink:#2a1430;
  --white:#ffffff;
  --grey:#9a9a9a;
}
*{margin:0;padding:0;box-sizing:border-box}
html,body{width:1200px;height:4971px;overflow:hidden;background:var(--white)}
body{position:relative;font-family:"Montserrat",sans-serif;color:var(--ink)}
.abs{position:absolute}
.display{font-family:"Syncopate",sans-serif;font-weight:700;letter-spacing:1px;text-transform:uppercase}
.play{position:absolute;border-radius:50%;background:var(--white);display:flex;align-items:center;justify-content:center}
.play svg{width:34%;height:34%}
.learn{position:absolute;display:flex;align-items:center;gap:12px;font-size:13px;font-weight:700;letter-spacing:1.5px;text-transform:uppercase}
.learn .dot{width:30px;height:30px;border-radius:50%;display:flex;align-items:center;justify-content:center}
.body-copy{font-size:14.5px;line-height:21px}
.body-copy p+p{margin-top:10px}

/* hero */
.hero{left:0;top:0;width:1200px;height:714px;border-bottom-left-radius:210px;overflow:hidden;
  background:linear-gradient(100deg,#3a1a3d 0%,#5a4250 45%,#4e3a46 70%,#2e1d2c 100%)}
.hero-chevron{left:560px;top:70px}
.logo{display:flex;flex-direction:column;align-items:flex-end;color:var(--white);font-family:"Montserrat",sans-serif;font-weight:500}
.logo .big{font-size:30px;line-height:30px;letter-spacing:1px}
.logo .small{font-size:12px;letter-spacing:1px}
.nav{top:34px;font-family:"Syncopate",sans-serif;font-size:11px;font-weight:700;color:var(--white);letter-spacing:.5px}
.contact-btn{left:914px;top:25px;width:130px;height:33px;border-radius:10px;background:var(--coral);color:var(--white);font-family:"Syncopate",sans-serif;font-size:11px;font-weight:700;display:flex;align-items:center;justify-content:center}
.hero h1{left:122px;top:236px;font-size:52px;line-height:58px;color:var(--white)}
.hero .tag{left:136px;top:432px;font-size:19px;color:var(--white)}
.scroll{left:1140px;top:234px;width:30px;height:226px}
.scroll .line{position:absolute;left:14px;top:0;width:2px;height:76px;background:var(--white)}
.scroll .txt{position:absolute;left:-48px;top:150px;transform:rotate(-90deg);font-size:11px;letter-spacing:2px;color:var(--white);white-space:nowrap;font-weight:600}

/* who */
.who-box{left:172px;top:816px;width:860px;height:266px;border:4px solid var(--grey)}
.who-title{left:0;top:792px;width:1200px;display:flex;justify-content:center}
.who-title span{background:var(--white);padding:0 22px;font-size:40px;color:var(--plum);display:flex;align-items:center;gap:10px}
.who-copy{left:232px;top:880px;width:740px;text-align:center;font-size:16px;line-height:23px;color:var(--ink)}
.who-copy p+p{margin-top:12px}
.down{left:577px;top:1055px;width:54px;height:54px;border-radius:50%;background:var(--coral);display:flex;align-items:center;justify-content:center}

/* programs */
.prog-coral{left:0;top:1190px;width:1200px;height:600px;background:var(--coral);border-top-right-radius:190px}
.prog-plum{left:0;top:1727px;width:1200px;height:621px;background:var(--plum);border-bottom-left-radius:190px}
.prog-title{left:0;top:1256px;width:1170px;text-align:center;font-size:40px;color:var(--white)}
.photo{position:absolute}
.p1{left:0;top:1370px;width:629px;height:415px;background:linear-gradient(120deg,#c9a882,#7f6a55 45%,#2c2a33)}
.p2{left:584px;top:1900px;width:616px;height:494px;background:linear-gradient(110deg,#d8d2c8,#a99f94 40%,#3c3442 85%)}
.p3{left:60px;top:2498px;width:577px;height:388px;background:linear-gradient(120deg,#2d3f7a,#5a4b6a 45%,#c48a2a 60%,#25345e)}
.prog-block h3{font-size:27px}
.first{left:677px;top:1404px;width:420px;color:var(--white)}
.first .body-copy{margin-top:18px}
.second{left:133px;top:1912px;width:410px;color:var(--white)}
.second .body-copy{margin-top:18px}
.third-bg{left:0;top:2436px;width:494px;height:548px;background:var(--blush);border-top-right-radius:110px}
.third{left:690px;top:2568px;width:420px;color:var(--ink)}
.third h3{color:var(--plum)}
.third .body-copy{margin-top:16px}
.fourth{left:0;top:2984px;width:1200px;height:566px;border-top-left-radius:250px;border-bottom-right-radius:250px;
  background:radial-gradient(ellipse at 32% 40%,#2b6a63 0%,#0c504d 45%,#0a4543 100%)}
.fourth h3{position:absolute;left:0;top:3194px;width:1200px;text-align:center;font-size:27px;color:var(--white)}
.fourth-copy{left:282px;top:3246px;width:636px;text-align:center;color:var(--white)}

/* testimonials */
.testi-title{left:0;top:3600px;width:1200px;text-align:center;font-size:40px;color:var(--plum)}
.card{position:absolute;top:3690px;height:342px}
.card .cap{position:absolute;left:0;bottom:22px;width:100%;text-align:center;color:var(--white);font-size:17px;line-height:21px}
.c1{left:0;width:397px;background:linear-gradient(180deg,#6e6a68,#3a3a45 70%,#22222b)}
.c2{left:405px;width:396px;background:linear-gradient(180deg,#a4998c,#55504d 60%,#262628)}
.c3{left:808px;width:392px;background:linear-gradient(180deg,#b9c3c6,#7d8b8a 45%,#1f4a4c 85%)}

/* contact */
.foot-bg{left:0;top:4442px;width:1200px;height:529px;background:var(--plum)}
.start-card{left:174px;top:4122px;width:858px;height:465px;background:var(--blush);border-top-right-radius:115px;border-bottom-left-radius:115px}
.start-title{left:174px;top:4188px;width:858px;text-align:center;font-size:30px;line-height:38px;color:var(--plum)}
.field{position:absolute;background:var(--white);font-size:11px;color:#555;padding:14px 26px}
.send{left:521px;top:4481px;width:175px;height:46px;border-radius:23px;background:var(--coral);color:var(--white);font-size:11px;font-weight:700;letter-spacing:1px;display:flex;align-items:center;justify-content:center;gap:6px}

/* footer */
.f-logo{left:193px;top:4650px}
.f-logo .big{font-size:36px;line-height:36px}
.f-col{top:4652px;color:var(--white)}
.f-col h4{font-size:13px;font-weight:700;letter-spacing:.5px;margin-bottom:20px}
.f-col li{list-style:none;font-size:11.5px;margin-bottom:14px}
.f-row{display:flex;gap:12px;align-items:flex-start;font-size:11.5px;line-height:17px;margin-bottom:18px}
.social{display:flex;gap:14px;margin-top:16px}
.social span{width:18px;height:18px;border-radius:4px;background:var(--coral)}
.f-rule{left:0;top:4894px;width:1200px;height:1px;background:rgba(255,255,255,.35)}
.copy{left:0;top:4914px;width:1200px;text-align:center;font-size:11px;color:var(--white)}
</style>
</head>
<body>

<!-- Hero -->
<section class="abs hero" role="img" aria-label="Photo of a coaching group session in a bright office">
  <svg class="abs hero-chevron" width="420" height="560" viewBox="0 0 420 560">
    <path d="M20 60 Q0 40 30 20 L60 0 Q80 -8 100 10 L380 250 Q410 280 380 310 L100 550 Q80 568 60 550 L30 530 Q0 510 20 490 L230 280 Z" fill="#d8a6e8" opacity=".55"/>
  </svg>
</section>
<div class="abs logo" style="left:130px;top:22px"><span class="big">WAYFORM</span><span class="small">PROJECT</span></div>
<div class="abs nav" style="left:428px">WHO WE ARE</div>
<div class="abs nav" style="left:583px">OUR PROGRAMS</div>
<div class="abs nav" style="left:760px">TESTIMONIALS</div>
<div class="abs contact-btn">CONTACT US</div>
<h1 class="abs display hero-h" style="left:122px;top:236px;font-size:52px;line-height:58px;color:#fff">Life Coaching<br>and Career<br>Coaching</h1>
<div class="abs display" style="left:136px;top:432px;font-size:19px;color:#fff">Personal Wellbeing Services</div>
<div class="abs" style="left:726px;top:282px;width:84px;height:84px;border-radius:50%;background:var(--coral);border:4px solid rgba(255,255,255,.6);display:flex;align-items:center;justify-content:center">
  <svg width="28" height="28" viewBox="0 0 24 24"><path d="M7 4 L19 12 L7 20 Z" fill="none" stroke="#fff" stroke-width="2" stroke-linejoin="round"/></svg>
</div>
<div class="abs scroll"><div class="line"></div><div class="txt">‹ SCROLL DOWN</div></div>

<!-- Who we are -->
<div class="abs who-box"></div>
<div class="abs who-title"><span class="display">Who We Are<svg width="26" height="34" viewBox="0 0 26 34"><path d="M6 4 L20 17 L6 30" fill="none" stroke="var(--coral)" stroke-width="6"/></svg></span></div>
<div class="abs who-copy">
  <p>Lorem ipsum dolor sit amet, consectetur adipiscing elit, sed do eiusmod tempor incididunt ut labore et dolore magna aliqua. Ut enim ad minim veniam, quis nostrud exercitation ullamco laboris nisi ut aliquip ex ea</p>
  <p>Duis aute irure dolor in reprehenderit in voluptate velit esse cillum dolore eu fugiat nulla pariatur. Excepteur sint occaecat cupidatat non proident, sunt in</p>
</div>
<div class="abs down"><svg width="24" height="24" viewBox="0 0 24 24"><path d="M12 4 V19 M6 13 L12 19 L18 13" fill="none" stroke="#fff" stroke-width="2"/></svg></div>

<!-- Programs -->
<div class="abs prog-plum"></div>
<div class="abs prog-coral"></div>
<div class="abs display prog-title">Our Programs<svg width="26" height="34" viewBox="0 0 26 34" style="vertical-align:-4px;margin-left:6px"><path d="M6 4 L20 17 L6 30" fill="none" stroke="#fff" stroke-width="6"/></svg></div>

<div class="photo p1" role="img" aria-label="Photo of a woman speaking to a seated audience"></div>
<div class="play" style="left:322px;top:1508px;width:92px;height:92px"><svg viewBox="0 0 24 24"><path d="M7 4 L19 12 L7 20 Z" fill="none" stroke="#222" stroke-width="1.6" stroke-linejoin="round"/></svg></div>
<div class="abs prog-block first">
  <h3 class="display">First Programs</h3>
  <div class="body-copy"><p>Audiences want to know that your brand is authentic. That you will deliver what you promise and that you understand their challenges.</p><p>We write great B2B content that converts into sales – we tell stories that promote the value and benefits of your products and services to capture the attention</p></div>
</div>
<div class="learn" style="left:683px;top:1627px;color:#fff">Learn More<span class="dot" style="background:var(--teal)"><svg width="14" height="14" viewBox="0 0 14 14"><path d="M3 11 L11 3 M5 3 H11 V9" fill="none" stroke="#fff" stroke-width="1.5"/></svg></span></div>

<div class="abs prog-block second">
  <h3 class="display">Second Programs</h3>
  <div class="body-copy"><p>Lorem ipsum dolor sit amet, consectetur adipiscing elit, sed do eiusmod tempor incididunt ut labore et dolore magna aliqua. Ut enim ad minim veniam, quis nostrud exercitation ullamco laboris nisi ut aliquip ex ea</p><p>Duis aute irure dolor in reprehenderit in voluptate velit esse cillum dolore eu fugiat nulla pariatur. Excepteur sint occaecat cupidatat non proident, sunt in</p></div>
</div>
<div class="learn" style="left:138px;top:2153px;color:#fff">Learn More<span class="dot" style="background:var(--coral)"><svg width="14" height="14" viewBox="0 0 14 14"><path d="M3 11 L11 3 M5 3 H11 V9" fill="none" stroke="#fff" stroke-width="1.5"/></svg></span></div>
<div class="photo p2" role="img" aria-label="Photo of two women in a one-to-one coaching conversation"></div>
<div class="play" style="left:874px;top:2096px;width:92px;height:92px"><svg viewBox="0 0 24 24"><path d="M7 4 L19 12 L7 20 Z" fill="none" stroke="#222" stroke-width="1.6" stroke-linejoin="round"/></svg></div>

<div class="abs third-bg"></div>
<div class="photo p3" role="img" aria-label="Photo of a speaker in a yellow dress addressing a large audience"></div>
<div class="play" style="left:316px;top:2646px;width:92px;height:92px"><svg viewBox="0 0 24 24"><path d="M7 4 L19 12 L7 20 Z" fill="none" stroke="#222" stroke-width="1.6" stroke-linejoin="round"/></svg></div>
<div class="abs prog-block third">
  <h3 class="display">Third Program</h3>
  <div class="body-copy"><p>Lorem ipsum dolor sit amet, consectetur adipiscing elit, sed do eiusmod tempor incididunt ut labore et dolore magna aliqua. Ut enim ad minim veniam, quis nostrud exercitation ullamco laboris nisi ut aliquip ex ea</p><p>Duis aute irure dolor in reprehenderit in voluptate velit esse cillum dolore eu fugiat nulla pariatur. Excepteur sint occaecat cupidatat non proident, sunt in</p></div>
</div>
<div class="learn" style="left:696px;top:2800px;color:var(--plum)">Learn More<span class="dot" style="background:var(--plum)"><svg width="14" height="14" viewBox="0 0 14 14"><path d="M3 11 L11 3 M5 3 H11 V9" fill="none" stroke="#fff" stroke-width="1.5"/></svg></span></div>

<div class="abs fourth" role="img" aria-label="Teal-toned photo of a smiling woman speaking on stage"></div>
<div class="play" style="left:564px;top:3071px;width:96px;height:96px"><svg viewBox="0 0 24 24"><path d="M7 4 L19 12 L7 20 Z" fill="none" stroke="#222" stroke-width="1.6" stroke-linejoin="round"/></svg></div>
<h3 class="display" style="position:absolute;left:0;top:3194px;width:1200px;text-align:center;font-size:27px;color:#fff">Fourth Programs</h3>
<div class="abs body-copy fourth-copy"><p>Lorem ipsum dolor sit amet, consectetur adipiscing elit, sed do eiusmod tempor incididunt ut labore et dolore magna aliqua. Ut enim ad minim veniam, quis nostrud exercitation ullamco laboris nisi ut aliquip ex ea</p><p>Duis aute irure dolor in reprehenderit in voluptate velit esse cillum dolore eu fugiat nulla pariatur. Excepteur sint occaecat cupidatat non proident, sunt in</p></div>

<!-- Testimonials -->
<div class="abs display testi-title">Testimonials<svg width="26" height="34" viewBox="0 0 26 34" style="vertical-align:-4px;margin-left:6px"><path d="M6 4 L20 17 L6 30" fill="none" stroke="var(--coral)" stroke-width="6"/></svg></div>
<div class="card c1" role="img" aria-label="Video still of a smiling woman with glasses in a blazer"><div class="cap">Lorem ipsum dolor sit<br>amet consecte</div></div>
<div class="card c2" role="img" aria-label="Video still of a smiling man outdoors in a city"><div class="cap">Lorem ipsum dolor sit<br>amet consecte</div></div>
<div class="card c3" role="img" aria-label="Video still of a laughing woman on a beach"><div class="cap">Lorem ipsum dolor sit<br>amet consecte</div></div>
<div class="play" style="left:176px;top:3827px;width:68px;height:68px"><svg viewBox="0 0 24 24"><path d="M7 4 L19 12 L7 20 Z" fill="none" stroke="#222" stroke-width="1.8" stroke-linejoin="round"/></svg></div>
<div class="play" style="left:573px;top:3829px;width:68px;height:68px"><svg viewBox="0 0 24 24"><path d="M7 4 L19 12 L7 20 Z" fill="none" stroke="#222" stroke-width="1.8" stroke-linejoin="round"/></svg></div>
<div class="play" style="left:973px;top:3827px;width:68px;height:68px"><svg viewBox="0 0 24 24"><path d="M7 4 L19 12 L7 20 Z" fill="none" stroke="#222" stroke-width="1.8" stroke-linejoin="round"/></svg></div>

<!-- Contact -->
<div class="abs foot-bg"></div>
<div class="abs start-card"></div>
<div class="abs display start-title">Get Started with<br>Wayform Project<svg width="22" height="30" viewBox="0 0 26 34" style="vertical-align:-3px;margin-left:6px"><path d="M6 4 L20 17 L6 30" fill="none" stroke="var(--coral)" stroke-width="6"/></svg></div>
<div class="field" style="left:262px;top:4279px;width:336px;height:44px">First Name</div>
<div class="field" style="left:606px;top:4279px;width:335px;height:44px">Last Name</div>
<div class="field" style="left:262px;top:4335px;width:336px;height:46px">Email address</div>
<div class="field" style="left:606px;top:4335px;width:335px;height:46px">Phone</div>
<div class="field" style="left:262px;top:4390px;width:679px;height:78px;padding-top:10px">Message</div>
<div class="abs send">SEND MESSAGE<svg width="18" height="10" viewBox="0 0 18 10"><path d="M0 5 H16 M12 1 L16 5 L12 9" fill="none" stroke="#fff" stroke-width="1.3"/></svg></div>

<!-- Footer -->
<div class="abs logo f-logo"><span class="big">WAYFORM</span><span class="small">PROJECT</span></div>
<div class="abs f-col" style="left:448px">
  <h4>NAVIGATION</h4>
  <ul><li>About Us</li><li>Our Services</li><li>Why Choose Us</li><li>News</li><li>Contact Us</li></ul>
</div>
<div class="abs f-col" style="left:646px;width:230px">
  <h4>CONTACT US</h4>
  <div class="f-row"><svg width="20" height="24" viewBox="0 0 20 24"><path d="M10 1 C5 1 2 5 2 9 C2 15 10 23 10 23 C10 23 18 15 18 9 C18 5 15 1 10 1 Z" fill="#fff"/><circle cx="10" cy="9" r="3" fill="var(--plum)"/></svg><span>14 Harrow Quay,<br>#02-11 Fenwell House<br>Singapore 230418</span></div>
  <div class="f-row" style="align-items:center"><svg width="22" height="22" viewBox="0 0 22 22"><circle cx="11" cy="11" r="11" fill="#fff"/><path d="M7 6 L9 6 L10 9 L8.7 10 C9.5 11.7 10.5 12.7 12 13.3 L13 12 L16 13 L16 15 C11 16 6 11 7 6 Z" fill="var(--plum)"/></svg><span>+65 6100 4472</span></div>
  <div class="f-row" style="align-items:center"><svg width="22" height="22" viewBox="0 0 22 22"><circle cx="11" cy="11" r="11" fill="#fff"/><rect x="6" y="7.5" width="10" height="7" fill="none" stroke="var(--plum)" stroke-width="1.3"/><path d="M6 7.5 L11 11.5 L16 7.5" fill="none" stroke="var(--plum)" stroke-width="1.3"/></svg><span style="text-decoration:underline">hello@wayform.com</span></div>
</div>
<div class="abs f-col" style="left:903px">
  <h4>FOLLOW US</h4>
  <div style="font-size:11px;margin-top:-6px">Please connect with us</div>
  <div class="social"><span></span><span></span><span></span><span></span></div>
</div>
<div class="abs f-rule"></div>
<div class="abs copy">© 2024 Wayform Project All Rights Reserved</div>

</body>
</html>
```